Transport & Storage Company needs a revamp of current card

Would like to keep same colours & basic design but would like to "sharpen" up look of card.

Please remove "The Bright Haulers"

Please add 1800 419 386 on front & back of card

Please add email address on back of card - martin@brackenfreight.com.au

I would like our ABN No - 83 214 976 302 on back of card (which currently has logo only). Logo on back of card can be removed if insufficient space.

Please design another card (same as above) but with Donna Petherick - 0438 562 714, donna@brackenfreight.com.au

I do not want cards to look "too busy" so please re-arrange layout of card if necessary.

Target Market(s)

Transport & Storage

Industry/Entity Type

It Company

Contact Information for Business Card

Please refer to attached current business card

Font styles to use
Other font styles liked:
• Tahoma

Requirements
Must have
• Refer to project decsription
Nice to have
Should not have

```html
<!DOCTYPE html>
<html lang="en">
<head>
<meta charset="utf-8">
<title>Bracken Freight – Business Cards</title>
<link rel="stylesheet" href="https://fonts.googleapis.com/css2?family=Noto+Sans:wght@400;700&display=swap">
<style>
  :root {
    --purple: #6e3a8c;
    --grey: #58585a;
    --white: #ffffff;
    --grey-text: #e9e6ee;
    --backdrop: #e7e5e9;
    --font: "Noto Sans", Tahoma, sans-serif;
  }
  * { box-sizing: border-box; margin: 0; padding: 0; }
  html, body { width: 1200px; height: 892px; overflow: hidden; }
  body {
    background: var(--backdrop);
    font-family: var(--font);
    display: flex;
    align-items: center;
    justify-content: center;
    gap: 40px;
  }
  .card {
    position: relative;
    width: 540px;
    height: 330px;
    background: var(--white);
    box-shadow: 0 6px 18px rgba(0,0,0,0.18);
    overflow: hidden;
  }
  .card__bands { position: absolute; inset: 0; width: 100%; height: 100%; }
  .band-purple { fill: var(--purple); }
  .band-grey { fill: var(--grey); }

  .brand {
    position: absolute;
    display: flex;
    align-items: center;
    gap: 10px;
    color: var(--purple);
    font-weight: 700;
    white-space: nowrap;
  }
  .brand__dot {
    border-radius: 50%;
    background: var(--purple);
    flex: none;
  }

  .card--back .brand { left: 150px; top: 72px; font-size: 36px; }
  .card--back .brand__dot { width: 26px; height: 26px; }
  .abn {
    position: absolute;
    left: 188px; top: 130px;
    color: var(--purple);
    font-size: 14px;
  }

  .card--front .brand { right: 38px; top: 110px; font-size: 26px; }
  .card--front .brand__dot { width: 20px; height: 20px; }
  .holder-name {
    position: absolute;
    left: 34px; top: 28px;
    color: var(--purple);
    font-size: 19px;
    font-weight: 700;
  }

  .phones {
    position: absolute;
    left: 26px;
    color: var(--grey-text);
    font-size: 15px;
    line-height: 1.35;
    letter-spacing: 0.3px;
  }
  .card--back .phones { top: 206px; }
  .card--front .phones { top: 188px; }

  .band-text {
    position: absolute;
    left: 26px; bottom: 18px;
    color: var(--white);
    font-size: 16px;
    letter-spacing: 0.2px;
  }
</style>
</head>
<body>

  <article class="card card--back" aria-label="Card back">
    <svg class="card__bands" viewBox="0 0 540 330" aria-hidden="true">
      <polygon class="band-grey" points="0,170 528,260 0,252"/>
      <rect class="band-purple" x="0" y="268" width="540" height="62"/>
    </svg>
    <div class="brand"><span class="brand__dot"></span>Bracken Freight</div>
    <p class="abn">ABN No - 83 214 976 302</p>
    <p class="phones">1800 419 386</p>
    <p class="band-text">martin@brackenfreight.com.au</p>
  </article>

  <article class="card card--front" aria-label="Card front">
    <svg class="card__bands" viewBox="0 0 540 330" aria-hidden="true">
      <polygon class="band-grey" points="0,170 528,260 0,252"/>
      <rect class="band-purple" x="0" y="268" width="540" height="62"/>
    </svg>
    <h1 class="holder-name">Martin Haldane</h1>
    <div class="brand"><span class="brand__dot"></span>Bracken Freight</div>
    <p class="phones">0412 738 905<br>1800 419 386</p>
    <p class="band-text">www.brackenfreight.com.au</p>
  </article>

</body>
</html>
```